Lanternfall Theatre Co. Business Card Design

Lanternfall Theatre Co. are a not for profit performing arts group based in Marlbrook dedicated to creating entertaining and engaging theatre that tackles hard hitting subjects head on. We also offer private tutoring for anyone wishing to pursue a career in performing arts.
I want a business card that shows the contact information above and our company logo, I would like a business card that looks professional which is simple and effective.
Target Market(s)
Theatre goers and performing artists ranging from 14 to 65
Industry/Entity Type
Tutoring
Contact Information for Business Card
Gavin Pellow, Artistic Director
Address: Lanternfall Theatre Co. Ferris Lane, Marlbrook, West Vale, ML7 4QT
Tele: 07412 563917
Email: lanternfalltheatre@mailvista.example
Web: www.lanternfalltheatre.example
Facebook: www.facebook.com/lanternfalltheatreco42

```html
<!DOCTYPE html>
<html lang="en">
<head>
<meta charset="utf-8">
<title>Lanternfall Theatre Co. — Business Card</title>
<link href="https://fonts.googleapis.com/css2?family=Lato:wght@400;700&display=swap" rel="stylesheet">
<style>
  :root {
    --backdrop: #8a8a8a;
    --card: #ffffff;
    --ink: #1a1a1a;
    --accent: #e3262b;
  }
  * { margin: 0; padding: 0; box-sizing: border-box; }
  html, body {
    width: 1200px;
    height: 900px;
    overflow: hidden;
    background: var(--backdrop);
    font-family: "Lato", sans-serif;
    color: var(--ink);
  }
  .card {
    position: absolute;
    left: 100px;
    top: 140px;
    width: 1000px;
    height: 620px;
    background: var(--card);
  }
  .brand {
    position: absolute;
    left: 60px;
    top: 110px;
    width: 380px;
    display: flex;
    align-items: center;
    gap: 16px;
  }
  .brand-dot {
    flex: none;
    width: 34px;
    height: 34px;
    border-radius: 50%;
    background: var(--accent);
  }
  .brand-name {
    font-size: 28px;
    font-weight: 700;
    line-height: 1.2;
  }
  .person {
    position: absolute;
    right: 60px;
    top: 92px;
    text-align: right;
  }
  .person-name {
    font-size: 44px;
    color: var(--accent);
    letter-spacing: 1px;
    line-height: 1.1;
  }
  .person-name .given { font-weight: 400; }
  .person-name .family { font-weight: 700; }
  .person-role {
    margin-top: 10px;
    font-size: 20px;
    letter-spacing: 2.5px;
    text-transform: uppercase;
  }
  .contacts {
    position: absolute;
    right: 60px;
    top: 250px;
    list-style: none;
    text-align: right;
    font-size: 24px;
    line-height: 40px;
  }
  .contacts .label { display: inline-block; width: 22px; text-align: right; }
  .address {
    position: absolute;
    right: 60px;
    top: 460px;
    text-align: right;
    font-size: 20px;
    line-height: 42px;
    font-style: normal;
  }
</style>
</head>
<body>
  <article class="card">
    <div class="brand">
      <span class="brand-dot"></span>
      <span class="brand-name">Lanternfall Theatre Co.</span>
    </div>

    <header class="person">
      <h1 class="person-name"><span class="given">GAVIN</span> <span class="family">PELLOW</span></h1>
      <p class="person-role">Artistic Director</p>
    </header>

    <ul class="contacts">
      <li>07412 563917 : <span class="label">t</span></li>
      <li>lanternfalltheatre@mailvista.example : <span class="label">e</span></li>
      <li>www.lanternfalltheatre.example : <span class="label">w</span></li>
      <li>social.example/lanternfalltheatreco42 : <span class="label">s</span></li>
    </ul>

    <address class="address">
      Lanternfall Theatre Co. Ferris Lane,<br>
      Marlbrook, West Vale, ML7 4QT
    </address>
  </article>
</body>
</html>
```